Business card design needed

I need a business card for my Sydney Painting Business, that specialises in painting High -end residential homes. i want the design to look clean, modern and edgy. i also want a logo next to the RL Decorating, using RLD together.

Industry/Entity Type

Residential

Contact Information for Business Card

RL Decorating (business name),LIC 871536K, Rob Lindqvist, robert.lindqvist@brushmail.example, mobile 0419352807

```html
<!DOCTYPE html>
<html lang="en">
<head>
<meta charset="utf-8">
<title>RL Decorating – Business Card</title>
<link href="https://fonts.googleapis.com/css2?family=Cabin:wght@400;500;600;700&display=swap" rel="stylesheet">
<style>
  :root {
    --card-bg: #ffffff;
    --card-frame: #9a9a9a;
    --ink-black: #111111;
    --ink-grey: #6d6e70;
    --mark-rose: #d27380;
    --mark-red: #c1414f;
    --mark-crimson: #9e2830;
  }
  html, body {
    margin: 0;
    padding: 0;
    width: 1200px;
    height: 693px;
    overflow: hidden;
    background: var(--card-bg);
  }
  .card {
    position: relative;
    width: 1200px;
    height: 693px;
    box-sizing: border-box;
    border: 3px solid var(--card-frame);
    background: var(--card-bg);
    font-family: "Cabin", "Trebuchet MS", sans-serif;
  }
  .brand-initials {
    position: absolute;
    left: 0;
    right: 0;
    top: 118px;
    text-align: center;
    font-size: 232px;
    line-height: 1;
    font-weight: 700;
    letter-spacing: 2px;
    color: var(--ink-black);
    padding-right: 24px;
  }
  .brand-name {
    position: absolute;
    left: 0;
    right: 0;
    top: 348px;
    text-align: center;
    font-size: 70px;
    line-height: 1;
    font-weight: 500;
    color: var(--ink-grey);
    padding-right: 24px;
  }
  .contact-list {
    position: absolute;
    left: 0;
    right: 0;
    top: 502px;
    margin: 0;
    padding: 0 20px 0 0;
    list-style: none;
    text-align: center;
  }
  .contact-item {
    display: flex;
    justify-content: center;
    align-items: center;
    gap: 4px;
    color: var(--ink-grey);
    font-size: 32px;
    line-height: 45px;
    font-weight: 500;
  }
  .contact-item::before {
    content: "";
    width: 17px;
    height: 17px;
    margin-top: 6px;
    background: var(--bullet);
  }
  .contact-licence { --bullet: var(--mark-rose); }
  .contact-email { --bullet: var(--mark-red); }
  .contact-mobile {
    --bullet: var(--mark-crimson);
    color: var(--ink-black);
    font-weight: 600;
    font-size: 38px;
    line-height: 56px;
  }
</style>
</head>
<body>
  <main class="card">
    <div class="brand-initials">RLD</div>
    <div class="brand-name">RL Decorating</div>
    <ul class="contact-list">
      <li class="contact-item contact-licence">LIC 871536K, Rob Lindqvist</li>
      <li class="contact-item contact-email">robert.lindqvist@brushmail.example</li>
      <li class="contact-item contact-mobile">mobile: 0419352807</li>
    </ul>
  </main>
</body>
</html>
```